Billboard design 8x3M NURA (Spanish company)

We´re located in the south of Spain. We run a local telecom company.
We sell Fiber optic, and mobile phone lines mainly.
The billboard will have to be in Spanish, I would like the price to be something you spot on first sight when passing by in the car.
Our company color is blue, like in our logo which I will add. I will also add a example from what we currently have.
The new offer should be:
1000 megas + 100Gigas movil con llamadas ilimitadas. (meaning 1000Mb fiber optic speed and 100Gb data and unlimited calls for 1 mobile line)
Our details are: phone line 952 00 0147
Website: nu-ra.es

```html
<!DOCTYPE html>
<html lang="es">
<head>
<meta charset="UTF-8">
<title>NURA – Valla 8x3 Fibra + Movil</title>
<link rel="stylesheet" href="https://fonts.googleapis.com/css2?family=Anton&family=Archivo+Black&family=Poppins:wght@700;800&display=swap">
<style>
  :root {
    --page-bg: #a9a9a9;
    --navy-deep: #03094a;
    --navy: #0a1f7a;
    --royal: #1746b8;
    --sky-blue: #2196cf;
    --yellow: #e2c813;
    --red: #d40a0a;
    --white: #ffffff;
    --ink: #222222;
    --rocket-orange: #f0561a;
  }
  * { margin: 0; padding: 0; box-sizing: border-box; }
  html, body {
    width: 865px;
    height: 1200px;
    overflow: hidden;
    background: var(--page-bg);
  }
  .billboard {
    position: absolute;
    left: 62px;
    top: 813px;
    width: 747px;
    height: 280px;
    overflow: hidden;
  }
  .offer-panel {
    position: absolute;
    left: 0; top: 0;
    width: 747px;
    height: 206px;
    background:
      linear-gradient(172deg, transparent 44%, rgba(80,140,255,0.35) 50%, transparent 56%),
      linear-gradient(186deg, transparent 52%, rgba(60,120,240,0.25) 57%, transparent 62%),
      radial-gradient(ellipse at 25% 70%, rgba(40,90,210,0.55), transparent 60%),
      linear-gradient(90deg, var(--navy) 0%, var(--navy-deep) 55%, var(--navy) 100%);
  }
  .headline {
    position: absolute;
    font-family: "Archivo Black", sans-serif;
    line-height: 1;
    white-space: nowrap;
    font-weight: 400;
  }
  .headline--fibra {
    left: 38px; top: 27px;
    font-size: 45px;
    color: var(--sky-blue);
    letter-spacing: -0.5px;
  }
  .headline--precio {
    left: 38px; top: 76px;
    font-size: 26.5px;
    color: var(--white);
    letter-spacing: 0;
  }
  .plus-badge {
    position: absolute;
    border-radius: 50%;
    background: var(--red);
  }
  .plus-badge svg { display: block; width: 100%; height: 100%; }
  .plus-badge--large { left: 281px; top: 31px; width: 36px; height: 36px; }
  .plus-badge--small {
    left: 138px; top: 142px; width: 23px; height: 23px;
    background: var(--white);
    border: 2px solid var(--navy-deep);
  }
  .headline--movie {
    left: 336px; top: 29px;
    font-family: "Anton", sans-serif;
    font-size: 84px;
    color: var(--yellow);
    letter-spacing: 0;
  }
  .rule {
    position: absolute;
    left: 38px; top: 112px;
    width: 488px; height: 1px;
    background: rgba(255,255,255,0.55);
  }
  .spec-box {
    position: absolute;
    top: 125px;
    width: 101px; height: 56px;
    border-radius: 8px;
    text-align: center;
    font-family: "Archivo Black", sans-serif;
    line-height: 1;
    padding-top: 6px;
  }
  .spec-box__value { display: block; font-size: 28px; letter-spacing: -0.5px; }
  .spec-box__unit { display: block; font-size: 18px; margin-top: -1px; }
  .spec-box--megas { left: 38px; background: var(--yellow); }
  .spec-box--megas .spec-box__value { color: var(--red); }
  .spec-box--megas .spec-box__unit { color: var(--ink); }
  .spec-box--gigas { left: 161px; background: var(--sky-blue); }
  .spec-box--gigas .spec-box__value { color: var(--navy-deep); }
  .spec-box--gigas .spec-box__unit { color: var(--white); }
  .mobile-terms {
    position: absolute;
    left: 272px; top: 125px;
    font-family: "Poppins", sans-serif;
    font-weight: 800;
    font-size: 15.5px;
    line-height: 19px;
    color: var(--white);
  }
  .price-divider {
    position: absolute;
    left: 373px; top: 128px;
    width: 1px; height: 50px;
    background: rgba(255,255,255,0.7);
  }
  .price {
    position: absolute;
    left: 390px; top: 119px;
    font-family: "Anton", sans-serif;
    font-size: 68px;
    line-height: 1;
    color: var(--red);
    letter-spacing: -1px;
  }
  .hero-illustration {
    position: absolute;
    left: 543px; top: 0;
    width: 204px; height: 206px;
    background:
      radial-gradient(ellipse at 48% 35%, rgba(240,86,26,0.55), transparent 35%),
      radial-gradient(ellipse at 55% 70%, rgba(30,110,230,0.7), transparent 60%),
      linear-gradient(160deg, var(--navy-deep), var(--royal));
  }
  .contact-band {
    position: absolute;
    left: 0; top: 206px;
    width: 747px; height: 74px;
    background: var(--white);
  }
  .brand {
    position: absolute;
    left: 38px; top: 8px;
  }
  .brand__name {
    display: block;
    font-family: "Archivo Black", sans-serif;
    font-size: 36px;
    line-height: 1;
    color: var(--sky-blue);
    letter-spacing: 1px;
  }
  .brand__services {
    display: block;
    margin-top: 6px;
    font-family: "Poppins", sans-serif;
    font-weight: 700;
    font-size: 10px;
    color: var(--sky-blue);
    letter-spacing: 0.2px;
  }
  .contact-line {
    position: absolute;
    left: 189px; top: 10px;
    font-family: "Archivo Black", sans-serif;
    font-size: 42px;
    line-height: 1;
    color: var(--ink);
    white-space: nowrap;
    letter-spacing: 1.5px;
  }
  .contact-line__divider {
    display: inline-block;
    width: 3px; height: 38px;
    margin: 0 12px 0 10px;
    vertical-align: -6px;
    background: var(--sky-blue);
  }
  .contact-line__web { letter-spacing: 0; }
</style>
</head>
<body>
  <main class="billboard">
    <section class="offer-panel">
      <h1 class="headline headline--fibra">TU FIBRA</h1>
      <div class="plus-badge plus-badge--large">
        <svg viewBox="0 0 36 36"><path d="M18 9.5v17M9.5 18h17" stroke="#fff" stroke-width="4.5" stroke-linecap="round"/></svg>
      </div>
      <p class="headline headline--precio">AL MEJOR PRECIO</p>
      <p class="headline headline--movie">MOVIE</p>
      <div class="rule"></div>

      <div class="spec-box spec-box--megas">
        <span class="spec-box__value">1000</span>
        <span class="spec-box__unit">MEGAS</span>
      </div>
      <div class="plus-badge plus-badge--small">
        <svg viewBox="0 0 19 19"><path d="M9.5 4.5v10M4.5 9.5h10" stroke="#03094a" stroke-width="2.6" stroke-linecap="round"/></svg>
      </div>
      <div class="spec-box spec-box--gigas">
        <span class="spec-box__value">100</span>
        <span class="spec-box__unit">GIGAS</span>
      </div>

      <p class="mobile-terms">Movil con<br>llamadas<br>ilimitadas</p>
      <div class="price-divider"></div>
      <p class="price">35€</p>

      <div class="hero-illustration" role="img" aria-label="Ilustración isométrica de un cohete despegando desde un portátil sobre fondo azul"></div>
    </section>

    <footer class="contact-band">
      <div class="brand">
        <span class="brand__name">NURA</span>
        <span class="brand__services">Wifi | Fibra | Movil | Tv</span>
      </div>
      <p class="contact-line">
        <span class="contact-line__phone">952 00 0147</span><span class="contact-line__divider"></span><span class="contact-line__web">NU-RA.ES</span>
      </p>
    </footer>
  </main>
</body>
</html>
```